Restaurant needs a vertical banner for fried catfish

Our restaurant is looking for an eye-catching 78.75in. x 36in. vertical physical banner ad for our fried catfish. Photos for the fried catfish will be provided as a reference but we will also accept anything similar to the photo. We will be using the following as our receptacle: https://www.plankoria.example/banner-stand/retractable-banner-stands/
The design must incorporate the following flavor texts:
Fried Catfish
Always Fresh!
Made from Scratch
Hand-cut Fillets
The Best Catfish in Texas
Served with fries, hush puppies, and a 32oz fountain drink
Also available by the pound!
The final design should be creative, professional, and eye-catching for customers.
Updates
Colors
Designer to choose colors to be used in the design.
Requirements
Must have
- We are open to any and all design elements, albeit the 'flavor texts' should not overpower, but complement the fried catfish photo. 'Fried Catfish' can be used in lieu of a main title/logo.
Nice to have
- Transparent or textured backgrounds that can encompass any or all part of the banner such as a cutting board, shadows, abstract, etc to show depth are a plus.
- Use of vectors or objects such as ribbons or shapes to encapsulate the 'flavor texts' are also encouraged.

```html
<!DOCTYPE html>
<html lang="en">
<head>
<meta charset="utf-8">
<title>Fried Catfish Vertical Banner</title>
<link href="https://fonts.googleapis.com/css2?family=Anton&family=Arimo:wght@400;700&family=Berkshire+Swash&family=Oswald:wght@400;600&display=swap" rel="stylesheet">
<style>
  :root {
    --canvas: #f3f3f1;
    --banner: #e6e6e6;
    --forest: #254a1c;
    --lime: #cfde4a;
    --ink: #1b1b1b;
    --rust: #b4581e;
  }
  * { margin: 0; padding: 0; box-sizing: border-box; }
  html, body {
    width: 1200px; height: 1200px; overflow: hidden;
    background: var(--canvas);
  }
  .stage { position: relative; width: 1200px; height: 1200px; }
  .banner {
    position: absolute; left: 351px; top: 30px;
    width: 568px; height: 1303px;
    background: var(--banner);
    transform: scale(0.875); transform-origin: top left;
    overflow: hidden;
    box-shadow: 0 6px 18px rgba(0,0,0,0.18);
  }
  .hero { position: absolute; left: 0; top: 0; width: 568px; height: 480px; }
  .badge {
    position: absolute; left: 317px; top: 257px;
    width: 200px; height: 200px; border-radius: 50%;
    background: var(--lime); border: 5px solid var(--forest);
    display: flex; align-items: center; justify-content: center;
    text-align: center;
    font-family: "Berkshire Swash", cursive;
    color: var(--forest); font-size: 50px; line-height: 0.95;
    transform: rotate(-4deg);
  }
  .headline { position: absolute; left: 35px; top: 500px; }
  .title {
    font-family: "Anton", sans-serif; color: var(--forest);
    font-size: 80px; line-height: 1; letter-spacing: 0.5px;
  }
  .made {
    font-family: "Anton", sans-serif; color: var(--ink);
    font-size: 64px; line-height: 1; margin-top: 14px;
  }
  .scratch {
    font-family: "Anton", sans-serif; color: var(--ink);
    font-size: 104px; line-height: 0.95; letter-spacing: 1px;
  }
  .fillets {
    font-family: "Arimo", sans-serif; color: var(--ink);
    font-size: 50px; line-height: 1.1; margin-top: 4px;
  }
  .ribbon {
    position: absolute; left: 12px; top: 857px;
    width: 544px; height: 66px; background: var(--lime);
    display: flex; align-items: center; justify-content: center;
    font-family: "Arimo", sans-serif; color: var(--ink); font-size: 39px;
  }
  .ribbon-shadow { position: absolute; left: 60px; top: 918px; }
  .served { position: absolute; left: 49px; top: 955px; }
  .served-label {
    font-family: "Oswald", sans-serif; font-weight: 600;
    color: var(--rust); font-size: 26px; line-height: 1.2;
  }
  .served-items {
    font-family: "Oswald", sans-serif; font-weight: 400;
    color: var(--ink); font-size: 20px; line-height: 1.3;
  }
  .by-pound {
    position: absolute; left: 0; top: 1055px; width: 568px;
    text-align: center; padding-left: 50px;
    font-family: "Arimo", sans-serif; color: var(--ink); font-size: 27px;
  }
  .by-pound strong { font-weight: 700; }
  .by-pound .dotted {
    border-bottom: 4px dotted var(--rust); padding-bottom: 4px;
  }
  .footer-band {
    position: absolute; left: 0; top: 1236px;
    width: 568px; height: 33px; background: var(--forest);
  }
</style>
</head>
<body>
<div class="stage">
  <div class="banner">
    <svg class="hero" viewBox="0 0 568 480" width="568" height="480">
      <defs>
        <linearGradient id="platter" x1="0" y1="0" x2="1" y2="1">
          <stop offset="0" stop-color="#b9402e"/>
          <stop offset="0.25" stop-color="#b7852e"/>
          <stop offset="0.6" stop-color="#9c6a22"/>
          <stop offset="1" stop-color="#e3b760"/>
        </linearGradient>
      </defs>
      <path role="img" aria-label="Photo of golden fried catfish fillets with fries, hush puppies, tomato and tartar sauce"
            d="M0 0 H568 V220 L60 465 Q30 478 12 455 L0 440 Z" fill="url(#platter)"/>
      <polygon points="110,470 568,215 568,236 150,470" fill="var(--lime)"/>
      <polygon points="500,0 568,0 568,130" fill="var(--forest)"/>
    </svg>

    <div class="badge">Always<br>Fresh!</div>

    <div class="headline">
      <div class="title">FRIED CATFISH</div>
      <div class="made">Made from</div>
      <div class="scratch">Scratch</div>
      <div class="fillets">Hand-Cut Fillets</div>
    </div>

    <svg class="ribbon-shadow" width="450" height="14" viewBox="0 0 450 14">
      <path d="M0 2 Q225 14 450 2 Q225 8 0 2 Z" fill="#111"/>
    </svg>
    <div class="ribbon">★ The Best Catfish in Texas ★</div>

    <div class="served">
      <div class="served-label">Served with:</div>
      <div class="served-items">Fries | Hush Puppies | and a 32oz Fountain Drink</div>
    </div>

    <div class="by-pound">Also <strong>available</strong> by <span class="dotted">the pound!</span></div>

    <div class="footer-band"></div>
  </div>
</div>
</body>
</html>
```